Create modern and sleek business card for luxury real estate company

We're a "boutique" real estate office looking for a design that gets across a highly modern luxury brand. Blacks and whites are probably the best colors unless we try a silver foil for the logo. I've attached a version of our current logo here. I'd like to swap out the current font on there with Gotham Light Regular.

I'm looking to have one side of the card have the logo with the space for our agents info on the other side.

Target Market(s)

Young professionals in a "luxury" headspace

Industry/Entity Type

Real estate

Contact Information for Business Card

A place for agent name, cell number, website. The slogan "Quietly Redefining Every Address".

Font styles to use
Other font styles liked:
• Gotham Regular

Colors

Designer to choose only greyscale colors for use in the design.

Requirements
Must have
• Matte black as the background color. Clean lines and use of contrast. A specific design aspect that will use silver foil.
Nice to have
• Up in the air on integrating a QR code
Should not have
• Any houses or other real estate related design (ex: a clip art house)

```html
<!DOCTYPE html>
<html lang="en">
<head>
<meta charset="utf-8">
<title>Halden Realty – Business Card</title>
<link href="https://fonts.googleapis.com/css2?family=Montserrat:wght@300;400&display=swap" rel="stylesheet">
<style>
  :root {
    --page: #e9e9e9;
    --card-white: #f4f4f5;
    --card-black: #262627;
    --ink: #1e1e1e;
    --ink-soft: #3a3a3a;
    --rule: #2a2a2a;
    --silver: #c9c9cb;
  }
  * { box-sizing: border-box; margin: 0; padding: 0; }
  html, body {
    width: 826px; height: 1200px; overflow: hidden;
    background: var(--page);
    font-family: "Montserrat", "Helvetica Neue", Arial, sans-serif;
    font-weight: 300;
  }
  .sheet {
    width: 826px; height: 1200px;
    display: flex; flex-direction: column; align-items: center; justify-content: center;
    gap: 90px;
  }
  .card {
    position: relative;
    width: 630px; height: 360px;
    border-radius: 22px;
    box-shadow: 0 10px 30px rgba(0,0,0,.18);
  }
  /* Front: agent details */
  .card--front { background: var(--card-white); color: var(--ink); }
  .tagline {
    position: absolute; left: 44px; top: 104px;
    font-size: 23px; letter-spacing: .5px; color: var(--ink);
  }
  .brand-mark {
    position: absolute; right: 40px; top: 34px;
    display: flex; align-items: center; gap: 12px;
  }
  .brand-mark__circle {
    width: 58px; height: 58px; border: 2.5px solid var(--ink); border-radius: 50%;
  }
  .brand-mark__name {
    font-size: 16px; letter-spacing: 2px; text-transform: uppercase; color: var(--ink);
  }
  .agent { position: absolute; left: 64px; top: 170px; }
  .agent__name { font-size: 33px; font-weight: 400; letter-spacing: .5px; line-height: 1; }
  .agent__title { font-size: 13px; margin-top: 5px; color: var(--ink-soft); letter-spacing: .3px; }
  .rule {
    position: absolute; left: 64px; right: 44px; top: 234px;
    height: 1.5px; background: var(--rule);
  }
  .address {
    position: absolute; left: 80px; top: 252px;
    font-size: 14px; line-height: 1.5; color: var(--ink-soft); font-style: normal;
  }
  .contacts {
    position: absolute; right: 44px; top: 252px;
    list-style: none; font-size: 14px; line-height: 1.6; color: var(--ink-soft);
  }
  .contacts li { display: flex; align-items: center; gap: 9px; }
  .contacts svg { width: 13px; height: 13px; fill: var(--ink); flex: none; }

  /* Back: brand side */
  .card--back {
    background: var(--card-black);
    display: flex; align-items: center; justify-content: center; gap: 26px;
  }
  .brand-lockup__circle {
    width: 86px; height: 86px; border: 3px solid var(--silver); border-radius: 50%;
  }
  .brand-lockup__text { display: flex; flex-direction: column; align-items: center; }
  .brand-lockup__word {
    font-size: 46px; font-weight: 400; letter-spacing: 4px;
    text-transform: uppercase; color: var(--silver); line-height: 1.1;
  }
  .brand-lockup__rule { width: 100%; height: 3px; background: var(--silver); margin: 6px 0; }
</style>
</head>
<body>
<main class="sheet">
  <section class="card card--front" aria-label="Card front with agent details">
    <p class="tagline">Quietly Redefining Every Address</p>
    <div class="brand-mark">
      <span class="brand-mark__circle"></span>
      <span class="brand-mark__name">Halden Realty</span>
    </div>
    <div class="agent">
      <h1 class="agent__name">Mara Ellison</h1>
      <p class="agent__title">President &amp; Principal Broker</p>
    </div>
    <div class="rule"></div>
    <address class="address">48 Alder Lane<br>Westbrook, MA 02140<br>United States</address>
    <ul class="contacts">
      <li>
        <svg viewBox="0 0 24 24" aria-hidden="true"><path d="M6.6 10.8a15 15 0 0 0 6.6 6.6l2.2-2.2a1 1 0 0 1 1-.25 11.4 11.4 0 0 0 3.6.57 1 1 0 0 1 1 1V20a1 1 0 0 1-1 1A17 17 0 0 1 3 4a1 1 0 0 1 1-1h3.5a1 1 0 0 1 1 1c0 1.250.2 2.450.57 3.6a1 1 0 0 1-.25 1z"/></svg>
        555-014-2270
      </li>
      <li>
        <svg viewBox="0 0 24 24" aria-hidden="true"><path d="M2 5h20v14H2z M2 5l10 8 10-8" fill="none" stroke="#1e1e1e" stroke-width="2.4"/></svg>
        info@haldenrealty.com
      </li>
      <li>
        <svg viewBox="0 0 24 24" aria-hidden="true"><circle cx="12" cy="12" r="9.5" fill="none" stroke="#1e1e1e" stroke-width="2"/><path d="M2.5 12h19M12 2.5c3 3 3 16 0 19M12 2.5c-3 3-3 16 0 19" fill="none" stroke="#1e1e1e" stroke-width="1.6"/></svg>
        www.haldenrealty.com
      </li>
    </ul>
  </section>

  <section class="card card--back" aria-label="Card back with brand name">
    <span class="brand-lockup__circle"></span>
    <div class="brand-lockup__text">
      <span class="brand-lockup__word">Halden</span>
      <span class="brand-lockup__rule"></span>
      <span class="brand-lockup__word">Realty</span>
    </div>
  </section>
</main>
</body>
</html>
```